Phone Repair Business Card

I need a business card for my mobile phone/ smart phone and tablet repair business based in New Zealand. My business name is "T.K. Repairs". I would like to see a designer make a modern phone related business card, which could incorporate something to do with the Vorlan Zeltox as this is our main repaired product. i like the dark Grey and lime green colours

```html
<!DOCTYPE html>
<html lang="en">
<head>
<meta charset="utf-8">
<title>T.K. Repairs – Business Card</title>
<link rel="stylesheet" href="https://fonts.googleapis.com/css2?family=Arimo:ital,wght@0,400;0,700;1,400&display=swap">
<style>
  :root {
    --backdrop: #dce3ef;
    --card-body: #f1f2f6;
    --card-edge: #d9dbe2;
    --hardware: #2b2b2e;
    --screen-dark: #1b1b1d;
    --screen-mid: #3a3b3e;
    --title-white: #ffffff;
    --tagline-grey: #2c2c2e;
    --lime: #7bc23a;
    --icon-white: #f4f4f4;
  }
  * { margin: 0; padding: 0; box-sizing: border-box; }
  html, body {
    width: 1200px; height: 900px; overflow: hidden;
    background: var(--backdrop);
    font-family: "Arimo", Arial, sans-serif;
  }
  .card {
    position: absolute; left: 375px; top: 85px;
    width: 450px; height: 720px;
    background: var(--card-body);
    border: 1px solid var(--card-edge);
    border-radius: 44px;
    box-shadow: 0 4px 10px rgba(0,0,0,0.18);
  }
  .card__camera {
    position: absolute; left: 50%; top: 22px; width: 14px; height: 14px;
    margin-left: -7px; border-radius: 50%; background: var(--hardware);
  }
  .card__speaker {
    position: absolute; left: 170px; top: 50px; width: 70px; height: 10px;
    border-radius: 5px; background: var(--card-body);
    border: 2px solid #8a8b90;
  }
  .card__sensor {
    position: absolute; left: 142px; top: 51px; width: 9px; height: 9px;
    border-radius: 50%; background: var(--hardware);
  }
  .card__home-button {
    position: absolute; left: 50%; top: 606px; width: 72px; height: 72px;
    margin-left: -36px; border-radius: 50%;
    border: 3px solid #b9bbc1;
    box-shadow: inset 0 -2px 3px rgba(0,0,0,0.15);
  }
  .screen {
    position: absolute; left: 20px; top: 92px; width: 410px; height: 505px;
    overflow: hidden;
  }
  .screen__backdrop {
    position: absolute; inset: 0;
    background: radial-gradient(ellipse at 45% 40%, var(--screen-mid) 0%, var(--screen-dark) 75%);
  }
  .brand-name {
    position: absolute; left: 44px; top: 64px;
    font-weight: 700; font-size: 52px; letter-spacing: -0.5px;
    color: var(--title-white);
    text-shadow: 3px 3px 3px rgba(0,0,0,0.85);
  }
  .tagline {
    position: absolute; left: 40px; top: 150px; width: 330px;
    text-align: center; font-style: italic; font-size: 20px; line-height: 22px;
    color: var(--tagline-grey);
    text-shadow: 0 1px 1px rgba(255,255,255,0.18);
  }
  .address {
    position: absolute; left: 92px; top: 246px;
    font-weight: 700; font-size: 22px; line-height: 29px;
    color: var(--lime);
    text-shadow: 1px 1px 2px rgba(0,0,0,0.9);
  }
  .contacts {
    position: absolute; left: 64px; top: 340px; list-style: none;
  }
  .contacts__item {
    display: flex; align-items: center; height: 31px;
    font-weight: 700; font-size: 22px;
    color: var(--lime);
    text-shadow: 1px 1px 2px rgba(0,0,0,0.9);
  }
  .contacts__icon { width: 24px; height: 22px; margin-right: 12px; flex: none; }
</style>
</head>
<body>
  <div class="card">
    <div class="card__camera"></div>
    <div class="card__sensor"></div>
    <div class="card__speaker"></div>

    <div class="screen">
      <div class="screen__backdrop" role="img" aria-label="Photograph of a shattered phone screen with white cracks on black glass"></div>

      <h1 class="brand-name">T.K. Repairs</h1>
      <p class="tagline">mobile phone/ smartphone<br>and tablet repair</p>

      <p class="address">PO Box 1234<br>Street address 123<br>tel: +1 2345 678 910</p>

      <ul class="contacts">
        <li class="contacts__item">
          <svg class="contacts__icon" viewBox="0 0 24 22" aria-hidden="true">
            <rect x="1.5" y="4" width="21" height="14" fill="none" stroke="var(--icon-white)" stroke-width="2"/>
            <polyline points="1.5,4 12,12.5 22.5,4" fill="none" stroke="var(--icon-white)" stroke-width="2"/>
          </svg>
          email@yourcompany.com
        </li>
        <li class="contacts__item">
          <svg class="contacts__icon" viewBox="0 0 24 22" aria-hidden="true">
            <rect x="3" y="1" width="19" height="19" fill="none" stroke="var(--icon-white)" stroke-width="2"/>
          </svg>
          .com/yourcompany
        </li>
        <li class="contacts__item">
          <svg class="contacts__icon" viewBox="0 0 24 22" aria-hidden="true">
            <circle cx="12.5" cy="11" r="9" fill="none" stroke="var(--icon-white)" stroke-width="2.2"/>
          </svg>
          www.yourcompany.com
        </li>
      </ul>
    </div>

    <div class="card__home-button"></div>
  </div>
</body>
</html>
```